Recycling Depot Business Card Design

We need a double sided business card for our recycling depot business. Please include name, position, address, phone, cell, fax, email and website address. Business card should match the colour scheme of our logo and look environmental but modern. I've attached a few business cards from Mintvale Works that I like.

Industry/Entity Type

Recycling

Contact Information for Business Card

Please include name, position, address, phone, cell, fax, email and website address.

Font styles to use
Sans Serif

Requirements
Must have
• Our Logo, Colour Scheme that matches our logo. Use of Colour Gradients and a custom look.

```html
<!DOCTYPE html>
<html lang="en">
<head>
<meta charset="utf-8">
<title>Loopfield Resource Recovery – Business Card</title>
<link rel="stylesheet" href="https://fonts.googleapis.com/css2?family=Montserrat:ital,wght@0,400;0,500;0,700;0,800;1,300&family=Open+Sans:wght@400;700&display=swap">
<style>
  :root{
    --bg:#2b3036;
    --green-deep:#0f6a2e;
    --green-mid:#2f8f38;
    --green-lite:#7cbd3c;
    --white:#ffffff;
    --ink-soft:rgba(255,255,255,.85);
  }
  *{margin:0;padding:0;box-sizing:border-box}
  html,body{width:1200px;height:900px;overflow:hidden;background:var(--bg)}
  .canvas{position:relative;width:1200px;height:900px}

  .card{position:absolute;border-radius:22px;overflow:hidden;box-shadow:0 10px 30px rgba(0,0,0,.35)}

  /* front side */
  .card-front{left:90px;top:150px;width:360px;height:620px;
    background:linear-gradient(150deg,var(--green-deep) 0%,var(--green-mid) 45%,var(--green-lite) 100%)}
  .card-front .pattern{position:absolute;inset:0;
    background:radial-gradient(circle at 30% 40%,rgba(255,255,255,.06),transparent 60%),
               linear-gradient(150deg,rgba(0,0,0,.05),rgba(255,255,255,.04))}
  .front-brand{position:absolute;left:40px;top:150px;display:flex;align-items:center;gap:14px}
  .brand-dot{width:46px;height:46px;border-radius:50%;background:var(--white)}
  .brand-name{font-family:"Open Sans",sans-serif;font-weight:700;font-size:52px;color:var(--white);letter-spacing:-.5px}
  .front-tagline{position:absolute;left:40px;top:230px;font-family:"Open Sans",sans-serif;font-weight:400;
    font-size:24px;color:var(--white);letter-spacing:.5px}

  /* back side */
  .card-back{left:520px;top:270px;width:600px;height:350px;
    background:linear-gradient(120deg,var(--green-deep) 20%,var(--green-mid) 60%,var(--green-lite) 100%)}
  .back-shape{position:absolute;inset:0}
  .back-brand{position:absolute;left:40px;top:80px;display:flex;align-items:center;gap:10px}
  .back-brand .brand-dot{width:30px;height:30px;background:var(--green-mid)}
  .back-brand .brand-name{font-family:"Open Sans",sans-serif;font-weight:700;font-size:30px;color:var(--green-mid)}
  .person{position:absolute;left:380px;top:70px;font-family:"Montserrat",sans-serif;color:var(--white)}
  .person-name{font-weight:800;font-size:22px;letter-spacing:1px}
  .person-role{font-weight:300;font-style:italic;font-size:16px;margin-top:2px;color:var(--ink-soft)}
  .contacts{position:absolute;left:330px;top:200px;list-style:none;font-family:"Montserrat",sans-serif;
    font-weight:500;font-size:11.5px;color:var(--white);letter-spacing:.4px;text-transform:uppercase}
  .contacts li{display:flex;align-items:flex-start;gap:9px;margin-bottom:7px;line-height:1.25}
  .contact-icon{flex:none;width:16px;height:16px;border-radius:50%;background:var(--green-lite);
    display:flex;align-items:center;justify-content:center}
  .contact-icon svg{width:9px;height:9px}
</style>
</head>
<body>
<main class="canvas">

  <section class="card card-front" aria-label="Card front">
    <div class="pattern" role="img" aria-label="Faint repeating brand pattern across the green gradient"></div>
    <div class="front-brand">
      <span class="brand-dot"></span>
      <span class="brand-name">Loopfield</span>
    </div>
    <p class="front-tagline">Resource Recovery</p>
  </section>

  <section class="card card-back" aria-label="Card back">
    <svg class="back-shape" viewBox="0 0 600 350" preserveAspectRatio="none" aria-hidden="true">
      <polygon points="0,0 300,0 370,90 150,215 0,215" fill="#ffffff"/>
    </svg>
    <div class="back-brand">
      <span class="brand-dot"></span>
      <span class="brand-name">Loopfield</span>
    </div>
    <div class="person">
      <p class="person-name">MARLO FENWICK</p>
      <p class="person-role">Job Title Here</p>
    </div>
    <ul class="contacts">
      <li><span class="contact-icon"><svg viewBox="0 0 10 10"><path d="M5 1 9 5H8v4H2V5H1z" fill="#fff"/></svg></span><span>Kerrow Lane Depot<br>North Dale Area</span></li>
      <li><span class="contact-icon"><svg viewBox="0 0 10 10"><path d="M1 5 9 1 6 9 5 6z" fill="#fff"/></svg></span><span>hello@loopfield.co</span></li>
      <li><span class="contact-icon"><svg viewBox="0 0 10 10"><path d="M2 1h2l1 2-1 1a5 5 0 0 0 2 2l1-1 2 1v2c-4 1-8-3-7-7z" fill="#fff"/></svg></span><span>+000 4821 7730 215<br>+012 5530 9184 662</span></li>
      <li><span class="contact-icon"><svg viewBox="0 0 10 10"><circle cx="5" cy="5" r="3.6" fill="none" stroke="#fff" stroke-width="1.2"/><path d="M1.4 5h7.2M5 1.4v7.2" stroke="#fff" stroke-width=".9"/></svg></span><span>www.loopfield.co</span></li>
    </ul>
  </section>

</main>
</body>
</html>
```